Nanotechnology meets nature cosmetic company needs label design. Name of the company is QuillaBloom

We are a cosmetic brand that combines nanotechnology with nature in the form of hemp extracts and essential oils, creating products that provide pain relief as well as stress reduction and relaxation. We have three different products and need three separate labels. We have a logo and would like to incorporate that into the label design. The colors are teal, black and gray. We would like to convey a message of combining nature with cutting edge cosmetic technology.
1. Topical pain lotion
2. Bath soak
3. Massage lotion
The logo is attached and I would just like the logo used and not the text below. The colors of the logo should be teal cross and "V" inside the gray lines that make up the circle with black color inside the circle. If this can't be done, I can send another logo.

```html
<!DOCTYPE html>
<html lang="en">
<head>
<meta charset="utf-8">
<title>QuillaBloom Labels</title>
<link href="https://fonts.googleapis.com/css2?family=Poppins:wght@300;400;600;700&display=swap" rel="stylesheet">
<style>
  :root{
    --bg-top:#e9e9e9;
    --bg-mid:#f3f3f3;
    --teal:#22b8a7;
    --teal-deep:#1fa896;
    --teal-light:#8ad9cf;
    --gray:#a3a3a3;
    --gray-soft:#efefef;
    --white:#ffffff;
  }
  *{margin:0;padding:0;box-sizing:border-box}
  html,body{width:1200px;height:2600px;overflow:hidden}
  body{font-family:"Poppins",sans-serif;background:var(--bg-mid)}
  .canvas{position:relative;width:1200px;height:2600px}
  .scene{position:relative;width:1200px;height:866px;
    background:linear-gradient(180deg,var(--bg-top) 0%,var(--bg-mid) 60%,#ececec 100%)}
  .scene--massage{height:868px}

  .lid{position:absolute;left:297px;top:468px;width:280px;height:280px;border-radius:50%;
    background:var(--white);box-shadow:0 0 0 1px #e0e0e0;display:flex;align-items:center;justify-content:center}

  .label{position:absolute;background:var(--white);overflow:hidden;box-shadow:0 0 0 1px #e0e0e0}
  .label--jar{left:628px;top:470px;width:268px;height:240px}
  .label--pump{left:483px;top:329px;width:223px;height:335px}
  .label--spray{left:491px;top:392px;width:209px;height:295px}

  .leaf-decor{position:absolute;left:0;top:0;width:100%;height:70px;
    background:linear-gradient(180deg,var(--gray-soft),var(--white))}

  .brand{display:flex;align-items:center;gap:6px;color:var(--teal);font-weight:600;font-size:14px;line-height:1}
  .brand__dot{flex:none;width:18px;height:18px;border-radius:50%;border:2.5px solid var(--gray)}
  .label .brand{position:absolute;left:0;right:0;justify-content:center}
  .label--jar .brand{top:66px}
  .label--pump .brand{top:83px}
  .label--spray .brand{top:76px}
  .lid .brand{font-size:22px;gap:9px}
  .lid .brand__dot{width:28px;height:28px;border-width:4px}

  .title{position:absolute;color:var(--teal);text-transform:uppercase;font-size:15px;line-height:16px;z-index:2}
  .title strong{display:block;font-weight:700}
  .title span{display:block;font-weight:300}
  .label--pump .title{left:30px;top:168px}
  .label--spray .title{left:29px;top:147px}
  .title--inline{left:0;right:0;top:122px;text-align:center;font-size:16px}
  .title--inline strong,.title--inline span{display:inline}

  .band{position:absolute;left:0;right:0;bottom:0}
  .label--jar .band{top:135px}
  .label--pump .band{top:207px}
  .label--spray .band{top:180px}
  .band svg{position:absolute;left:0;top:0;width:100%;height:22px;display:block}
  .band__body{position:absolute;left:0;right:0;top:20px;bottom:0;background:var(--teal)}
  .label--spray .band__body{background:linear-gradient(90deg,#52cabb 0%,var(--teal) 50%,var(--teal-deep) 100%)}
  .band__leaves{position:absolute;left:0;right:0;bottom:0;height:55px;
    background:linear-gradient(180deg,rgba(255,255,255,0),rgba(255,255,255,.1))}
  .band__text{position:absolute;top:22px;color:var(--white);font-size:8px;line-height:9px;font-weight:400}
  .label--jar .band__text{left:92px}
  .label--pump .band__text{left:31px;top:8px}
  .label--spray .band__text{left:30px;top:8px}
  .band__text small{display:block;font-size:5px;line-height:7px;margin-top:1px}
</style>
</head>
<body>
<main class="canvas">

  <section class="scene scene--bath">
    <div class="lid">
      <div class="brand"><span class="brand__dot"></span>QuillaBloom</div>
    </div>
    <article class="label label--jar">
      <div class="leaf-decor" role="img" aria-label="Light gray line-drawn leaves"></div>
      <div class="brand"><span class="brand__dot"></span>QuillaBloom</div>
      <h2 class="title title--inline"><strong>Bath</strong> <span>Soak</span></h2>
      <div class="band">
        <svg viewBox="0 0 100 10" preserveAspectRatio="none" aria-hidden="true">
          <path d="M0 3 C30 0 60 9 100 2 L100 10 L0 10 Z" fill="var(--teal-light)"/>
          <path d="M0 6 C30 3 60 11 100 5 L100 10 L0 10 Z" fill="var(--teal)"/>
        </svg>
        <div class="band__body">
          <div class="band__leaves" role="img" aria-label="White line-drawn leaves"></div>
          <p class="band__text">Natural cosmetics<br>with nanotechnology<small>16OZ (400ML)</small></p>
        </div>
      </div>
    </article>
  </section>

  <section class="scene scene--pain">
    <article class="label label--pump">
      <div class="leaf-decor" role="img" aria-label="Light gray line-drawn leaves"></div>
      <div class="brand"><span class="brand__dot"></span>QuillaBloom</div>
      <h2 class="title"><strong>Topical</strong><span>Pain Lotion</span></h2>
      <div class="band">
        <svg viewBox="0 0 100 10" preserveAspectRatio="none" aria-hidden="true">
          <path d="M0 3 C30 0 60 9 100 2 L100 10 L0 10 Z" fill="var(--teal-light)"/>
          <path d="M0 6 C30 3 60 11 100 5 L100 10 L0 10 Z" fill="var(--teal)"/>
        </svg>
        <div class="band__body">
          <div class="band__leaves" role="img" aria-label="White line-drawn leaves"></div>
          <p class="band__text">Natural cosmetics<br>with nanotechnology<small>10OZ (300ML)</small></p>
        </div>
      </div>
    </article>
  </section>

  <section class="scene scene--massage">
    <article class="label label--spray">
      <div class="leaf-decor" role="img" aria-label="Light gray line-drawn leaves"></div>
      <div class="brand"><span class="brand__dot"></span>QuillaBloom</div>
      <h2 class="title"><strong>Massage</strong><span>Lotion</span></h2>
      <div class="band">
        <svg viewBox="0 0 100 10" preserveAspectRatio="none" aria-hidden="true">
          <path d="M0 3 C30 0 60 9 100 2 L100 10 L0 10 Z" fill="var(--teal-light)"/>
          <path d="M0 6 C30 3 60 11 100 5 L100 10 L0 10 Z" fill="#52cabb"/>
        </svg>
        <div class="band__body">
          <div class="band__leaves" role="img" aria-label="White line-drawn leaves"></div>
          <p class="band__text">Natural cosmetics<br>with nanotechnology<small>8.4OZ (250ML)</small></p>
        </div>
      </div>
    </article>
  </section>

</main>
</body>
</html>
```